Neon Lodging Offers Website looking for new design

We are a online travel discounter based around hotel accommodations in Las Vegas. We need a wordpress design that will be used as our corporate cover page, and also for the affiliate pages. The current design can be viewed at http://postweaveforum.com/clients/neonoffer/ and the final design needs to include most of the navigation components. The affiliate pages will need a space to display the booking engine, for example, as shown at http://www.qrv.travel/marcoti. Our general color scheme is red/black, and the two logos we use are attached.

Because this is a crowded niche it is extremely important that we set ourselves apart in the design. The more visually stunning and out of the box the design, the better. The site needs to look distinctively different than anything else online. Since the overall layout is very basic and does not have to provide a lot of information, it leaves a lot of flexibility in design concepts.

We realize it is a truncated timetable, which is why the increased fee for your time and guaranteed payout.

Industry/Entity Type

Travel

```html
<!DOCTYPE html>
<html lang="en">
<head>
<meta charset="utf-8">
<title>Neon Lodging — Wholesale Hotel Rates</title>
<link rel="stylesheet" href="https://fonts.googleapis.com/css2?family=Oswald:wght@400;600;700&family=Open+Sans:wght@400;600;700&display=swap">
<style>
  :root {
    --red: #c0161c;
    --red-dark: #8e1116;
    --black: #0b0b0d;
    --page: #ebebeb;
    --ink: #3d3d3d;
    --muted: #6b6b6b;
    --field: #f7f7f9;
    --line: #d4d4d4;
    --white: #ffffff;
  }
  * { box-sizing: border-box; margin: 0; padding: 0; }
  html, body { width: 1073px; height: 1200px; overflow: hidden; }
  body {
    position: relative;
    background: var(--page);
    font-family: "Open Sans", Arial, sans-serif;
    color: var(--ink);
  }
  .abs { position: absolute; }

  /* header */
  .top-rule { left: 0; top: 0; width: 1073px; height: 4px; background: var(--red); }
  .site-header { left: 0; top: 4px; width: 1073px; height: 68px; background: var(--black); }
  .brand { left: 178px; top: 20px; display: flex; align-items: center; gap: 10px; }
  .brand-dot { width: 30px; height: 30px; border-radius: 50%; background: var(--red); }
  .brand-name { font-family: "Oswald", sans-serif; font-weight: 700; font-size: 25px; color: var(--red); letter-spacing: .2px; }
  .main-nav { left: 421px; top: 30px; font-size: 13px; color: #e6e6e6; }
  .main-nav a { color: inherit; text-decoration: none; position: absolute; white-space: nowrap; }
  .main-nav .sep { position: absolute; width: 1px; height: 14px; background: #555; top: 3px; }
  .main-nav .current { color: var(--red); }
  .lang { left: 880px; top: 33px; font-size: 10px; color: #ddd; }
  .login { left: 847px; top: 58px; font-size: 9px; color: #aaa; }

  /* hero */
  .hero {
    left: 0; top: 72px; width: 1073px; height: 442px;
    background: linear-gradient(180deg, #0c1d3a 0%, #1a3560 35%, #7a4a3a 62%, #b98f6a 75%, #2f3440 90%, #1a1d24 100%);
  }
  .hero-title {
    left: 168px; top: 262px; height: 33px; width: 648px; background: var(--red);
    font-family: "Oswald", sans-serif; font-weight: 600; font-size: 18.5px; color: var(--white);
    line-height: 33px; padding-left: 9px; letter-spacing: .1px; white-space: nowrap;
  }
  .hero-sub {
    left: 168px; top: 299px; height: 25px; width: 180px; background: var(--red-dark);
    font-family: "Oswald", sans-serif; font-size: 13px; color: var(--white);
    line-height: 25px; padding-left: 12px;
  }

  /* search bar */
  .search { left: 170px; top: 475px; width: 732px; height: 75px; background: var(--white); box-shadow: 0 1px 4px rgba(0,0,0,.25); }
  .search-intro { left: 0; top: 0; width: 161px; height: 75px; background: #f1f1f1; padding: 13px 0 0 9px; }
  .search-intro h2 { font-weight: 400; font-size: 14px; color: #222; }
  .search-intro p { font-size: 10.5px; color: var(--muted); line-height: 13px; margin: 3px 0 0 6px; }
  .field-label { font-size: 10.5px; color: #444; top: 14px; white-space: nowrap; }
  .field { top: 31px; height: 28px; border: 1px solid #cfcfcf; background: var(--white); font-size: 10px; color: #777; line-height: 26px; padding-left: 8px; white-space: nowrap; }
  .caret { position: absolute; right: 7px; top: 11px; width: 0; height: 0; border-left: 4px solid transparent; border-right: 4px solid transparent; border-top: 5px solid #555; }
  .cal { position: absolute; right: 6px; top: 7px; }
  .search-btn { left: 647px; top: 31px; width: 71px; height: 28px; background: var(--red); color: var(--white); font-size: 11px; line-height: 28px; text-align: center; }

  /* rooms */
  .room-photo { top: 582px; width: 224px; height: 110px; background: #f8f9fb; border: 1px solid #d6d6d6; }
  .room-title { top: 702px; font-size: 17px; font-weight: 400; color: #333; white-space: nowrap; }
  .room-title b { font-weight: 700; }
  .room-text { top: 725px; width: 185px; font-size: 9.2px; line-height: 13px; color: #d0404a; }

  .dotted { left: 194px; width: 689px; border-top: 1px dashed #9a9a9a; }

  .section-title { font-family: "Oswald", sans-serif; font-weight: 700; font-size: 19px; color: var(--ink); letter-spacing: .3px; }
  .section-title span { color: var(--red); }
  .about-row {
    left: 0; top: 882px; width: 1073px;
    display: flex; justify-content: center; gap: 26px;
    font-size: 9px; color: #555; white-space: nowrap; letter-spacing: -.1px;
  }

  /* contact */
  .map { left: 197px; top: 992px; width: 141px; height: 144px; background: linear-gradient(135deg, #f6f6f6, #ededed); border: 1px solid #d8d8d8; }
  .contact-label { left: 357px; font-size: 10px; color: #444; }
  .social { top: 1113px; width: 18px; height: 18px; border-radius: 50%; background: #c9c9c9; }
  .input { left: 568px; width: 284px; background: var(--field); border: 1px solid #dadada; font-size: 9.5px; color: #aaa; padding: 5px 7px; }

  /* footer */
  .site-footer { left: 0; top: 1157px; width: 1073px; height: 43px; background: var(--red); color: var(--white); font-size: 9.5px; }
  .site-footer .copy { left: 168px; top: 16px; }
  .footer-nav { right: 219px; top: 16px; display: flex; gap: 10px; }
</style>
</head>
<body>
  <div class="abs top-rule"></div>
  <header class="abs site-header"></header>
  <div class="abs brand"><div class="brand-dot"></div><div class="brand-name">Neon Lodging</div></div>
  <nav class="abs main-nav">
    <span class="sep" style="left:0"></span>
    <a class="current" style="left:29px">Home</a>
    <span class="sep" style="left:99px"></span>
    <a style="left:137px">Groups</a>
    <span class="sep" style="left:204px"></span>
    <a style="left:245px">Search Events</a>
    <span class="sep" style="left:346px"></span>
    <a style="left:380px">Contact us</a>
  </nav>
  <div class="abs lang">EN ▾</div>
  <div class="abs login">log in/register</div>

  <section class="abs hero" role="img" aria-label="Night view of the Las Vegas Strip with palm trees, neon hotel towers and light trails of traffic"></section>
  <h1 class="abs hero-title">GET WHOLESALE RATES ON HOTEL ACCOMMODATIONS WITH NEONLODGING.TRAVEL</h1>
  <div class="abs hero-sub">AMAZING PLACE TO DISCOVER</div>

  <form class="abs search">
    <div class="abs search-intro">
      <h2>Search for a rooom</h2>
      <p>Lorem ipsum solor sid<br>ahmed loresin vane.</p>
    </div>
    <div class="abs field-label" style="left:176px">Type of room:</div>
    <div class="abs field" style="left:176px;width:132px">Select a type of room<span class="caret"></span></div>
    <div class="abs field-label" style="left:315px">Check-in date:</div>
    <div class="abs field" style="left:315px;width:110px">DD/MM/YYYY
      <svg class="cal" width="12" height="12" viewBox="0 0 12 12"><rect x=".5" y=".5" width="11" height="11" fill="none" stroke="#888"/><path d="M0 4h12M4 4v8M8 4v8M0 8h12" stroke="#888"/></svg></div>
    <div class="abs field-label" style="left:432px">Check-out date:</div>
    <div class="abs field" style="left:432px;width:110px">DD/MM/YYYY
      <svg class="cal" width="12" height="12" viewBox="0 0 12 12"><rect x=".5" y=".5" width="11" height="11" fill="none" stroke="#888"/><path d="M0 4h12M4 4v8M8 4v8M0 8h12" stroke="#888"/></svg></div>
    <div class="abs field-label" style="left:549px">Adults:</div>
    <div class="abs field" style="left:549px;width:42px">1<span class="caret"></span></div>
    <div class="abs field-label" style="left:598px">Children:</div>
    <div class="abs field" style="left:598px;width:42px">0<span class="caret"></span></div>
    <div class="abs search-btn">Search now</div>
  </form>

  <div class="abs room-photo" style="left:169px" role="img" aria-label="Single room photo"></div>
  <div class="abs room-photo" style="left:425px" role="img" aria-label="Double room photo"></div>
  <div class="abs room-photo" style="left:680px" role="img" aria-label="Suite room photo"></div>
  <h3 class="abs room-title" style="left:169px">Single room <b>110 €</b></h3>
  <h3 class="abs room-title" style="left:425px">Double room <b>180 €</b></h3>
  <h3 class="abs room-title" style="left:680px">Suite room <b>210 €</b></h3>
  <p class="abs room-text" style="left:169px">Lorem ipsum dolor sit amet, consectetuer adipiscing elit, sed diam nonummy nibh euismod tincidunt ut laoreet dolore magna aliquam erat volutpat.</p>
  <p class="abs room-text" style="left:425px">Lorem ipsum dolor sit amet, consectetuer adipiscing elit, sed diam nonummy nibh euismod tincidunt ut laoreet dolore magna aliquam erat volutpat.</p>
  <p class="abs room-text" style="left:680px">Lorem ipsum dolor sit amet, consectetuer adipiscing elit, sed diam nonummy nibh euismod tincidunt ut laoreet dolore magna aliquam erat volutpat.</p>

  <div class="abs dotted" style="top:799px"></div>
  <h2 class="abs section-title" style="left:0;width:1073px;text-align:center;top:818px">ABOUT <span>NEONLODGING.TRAVEL</span></h2>
  <div class="abs about-row">
    <p>NeonLodging.Travel is a Global Hotel Provider based in Las Vegas, NV.</p>
    <p>|</p>
    <p>We provide hotel accommodations at wholesale pricess, for any size group, large or small.</p>
  </div>
  <div class="abs dotted" style="top:937px"></div>

  <h2 class="abs section-title" style="left:232px;top:957px">CONTACT <span>US NOW</span></h2>
  <h2 class="abs section-title" style="left:568px;top:957px">NEED <span>HELP ?</span></h2>
  <div class="abs map" role="img" aria-label="Location map"></div>
  <div class="abs contact-label" style="top:1008px">Name:</div>
  <div class="abs contact-label" style="top:1033px">Email:</div>
  <div class="abs contact-label" style="top:1061px">Phone:</div>
  <div class="abs contact-label" style="top:1090px">Address:</div>
  <div class="abs contact-label" style="top:1116px">Connect:</div>
  <div class="abs social" style="left:418px"></div>
  <div class="abs social" style="left:442px"></div>
  <div class="abs social" style="left:466px"></div>
  <div class="abs social" style="left:490px"></div>
  <div class="abs social" style="left:514px"></div>
  <div class="abs input" style="top:992px;height:24px">Full name...</div>
  <div class="abs input" style="top:1020px;height:24px">Email...</div>
  <div class="abs input" style="top:1048px;height:90px">Your message...</div>

  <footer class="abs site-footer">
    <div class="abs copy">© 2015 &nbsp; All Rights Reserved.</div>
    <nav class="abs footer-nav"><span>Home</span><span>Groups</span><span>Search Events</span><span>Contact</span></nav>
  </footer>
</body>
</html>
```